BUSINESS CARD - HALVERDINE RURAL SERVICES

I would like to create a business card for my fertilizer spreading business. I would like to incorporate my existing logo and also a description of the services offered. The business card will be given to farmers so must be kept simple but effective. It will also be left in stores so much also be eye catching in order to stand out from other cards.

Target Market(s)

FARMERS

Requirements
Must have
• FRONT OF CARD = EXISTING LOGO + "CUSTOMISED SPREADING" below the logo

REAR Of CARD = SERVICES OFFERED AND CONTACT DETAILS

- Bulk fertilizer including Lime, Gypsum, Manure & Compost
- Granular fertilizer including Single Super, Urea, Gran-am, & Custom Blends
- Modern equipment - Autosteer & Variable Rate Capable
- Friendly & Reliable Service
- Contact Gus: 0471 502 318
Nice to have
• utilize same color scheme as existing logo

```html
<!DOCTYPE html>
<html lang="en">
<head>
<meta charset="utf-8">
<title>Halverdine Rural Services – Business Card</title>
<link href="https://fonts.googleapis.com/css2?family=Lato:wght@400;700;900&display=swap" rel="stylesheet">
<style>
  :root {
    --bg: #e3e3e3;
    --orange: #f7981f;
    --charcoal: #58585a;
    --ink: #4a4a4c;
    --white: #ffffff;
  }
  * { box-sizing: border-box; margin: 0; padding: 0; }
  html, body { width: 1200px; height: 1200px; overflow: hidden; }
  body {
    background: var(--bg);
    font-family: "Lato", sans-serif;
    display: flex;
    flex-direction: column;
    align-items: center;
    justify-content: center;
    gap: 60px;
  }
  .card {
    width: 840px;
    height: 480px;
    position: relative;
    box-shadow: 0 8px 24px rgba(0,0,0,0.18);
  }
  .card--front { background: var(--white); display: flex; align-items: center; }
  .card--back {
    background: var(--orange);
    color: var(--white);
    display: flex;
    flex-direction: column;
    align-items: center;
    justify-content: center;
    gap: 30px;
  }

  .brand { display: flex; flex-direction: column; align-items: center; gap: 14px; text-align: center; }
  .brand__mark { width: 110px; height: 110px; border-radius: 50%; flex: none; }
  .brand__name { font-weight: 900; font-size: 34px; line-height: 1.05; letter-spacing: -0.5px; }
  .brand__tagline {
    font-weight: 700; font-size: 15px; letter-spacing: 4px; text-transform: uppercase;
    padding-top: 8px; border-top: 2px solid currentColor;
  }
  .card--front .brand { width: 420px; }
  .card--front .brand__mark { background: var(--charcoal); }
  .card--front .brand__name { color: var(--charcoal); }
  .card--front .brand__tagline { color: var(--orange); }
  .card--back .brand { gap: 10px; }
  .card--back .brand__mark { background: var(--white); width: 96px; height: 96px; }
  .card--back .brand__name { color: var(--white); }
  .card--back .brand__tagline { color: var(--white); }

  .divider { width: 1px; height: 260px; background: var(--ink); }

  .contact { padding-left: 34px; color: var(--ink); font-size: 17px; line-height: 1.4; }
  .contact__name { color: var(--orange); font-weight: 700; font-size: 26px; line-height: 1.1; }
  .contact__role { margin-bottom: 12px; }
  .contact__address { margin-bottom: 12px; }
  .contact__list { list-style: none; }
  .contact__list li { display: flex; align-items: center; gap: 10px; }
  .contact__icon { width: 15px; height: 15px; fill: var(--orange); flex: none; }

  .services { list-style: none; text-align: center; font-size: 19px; line-height: 1.5; }
</style>
</head>
<body>

<section class="card card--front">
  <div class="brand">
    <span class="brand__mark"></span>
    <span class="brand__name">Halverdine<br>Rural Services</span>
    <span class="brand__tagline">Customised Spreading</span>
  </div>
  <div class="divider"></div>
  <div class="contact">
    <p class="contact__name">Gus Pellow</p>
    <p class="contact__role">Co-founder</p>
    <p class="contact__address">48 Wattle Creek Road,<br>Merrivale</p>
    <ul class="contact__list">
      <li><svg class="contact__icon" viewBox="0 0 24 24"><path d="M6.6 10.8a15.1 15.1 0 0 0 6.6 6.6l2.2-2.2a1 1 0 0 1 1-.25 11.4 11.4 0 0 0 3.6.57 1 1 0 0 1 1 1V20a1 1 0 0 1-1 1A17 17 0 0 1 3 4a1 1 0 0 1 1-1h3.5a1 1 0 0 1 1 1c0 1.25.2 2.45.57 3.57a1 1 0 0 1-.25 1z"/></svg>+61 3 5512 7408</li>
      <li><svg class="contact__icon" viewBox="0 0 24 24"><rect x="6" y="2" width="12" height="20" rx="2"/></svg>0471 502 318</li>
      <li><svg class="contact__icon" viewBox="0 0 24 24"><path d="M2 5h20v14H2z M2 5l10 8 10-8"/></svg>gus@halverdinerural.com</li>
      <li><svg class="contact__icon" viewBox="0 0 24 24"><circle cx="12" cy="12" r="10"/></svg>www.halverdinerural.com</li>
    </ul>
  </div>
</section>

<section class="card card--back">
  <div class="brand">
    <span class="brand__mark"></span>
    <span class="brand__name">Halverdine<br>Rural Services</span>
    <span class="brand__tagline">Customised Spreading</span>
  </div>
  <ul class="services">
    <li>Modern equipment – Autosteer &amp; Variable Rate Capable</li>
    <li>Friendly &amp; Reliable Services</li>
    <li>Bulk fertilizer including Lime, Gypsum, Manure &amp; Composts</li>
    <li>Granular fertilizer including Single Super, Urea, Gran-am, &amp; Custom Blends</li>
  </ul>
</section>

</body>
</html>
```